Recycling Depot Business Card Design

We need a double sided business card for our recycling depot business. Please include name, position, address, phone, cell, fax, email and website address. Business card should match the colour scheme of our logo and look environmental but modern. I've attached a few business cards from Plume Kettle that I like.

Industry/Entity Type

Recycling

Contact Information for Business Card

Please include name, position, address, phone, cell, fax, email and website address.

Font styles to use
Sans Serif

Requirements
Must have
• Our Logo, Colour Scheme that matches our logo. Use of Colour Gradients and a custom look.

```html
<!DOCTYPE html>
<html lang="en">
<head>
<meta charset="UTF-8">
<title>Loopwise Business Card</title>
<link href="https://fonts.googleapis.com/css2?family=Poppins:wght@400;500;700&display=swap" rel="stylesheet">
<style>
  :root {
    --stage: #1d1f1e;
    --green-deep: #1b6b36;
    --green-mid: #5cae46;
    --green-light: #9ccd3c;
    --green-soft: #6abf45;
    --ink: #1e1e1e;
    --paper: #ffffff;
  }
  * { box-sizing: border-box; margin: 0; padding: 0; }
  html, body {
    width: 1200px; height: 1200px; overflow: hidden;
    background: var(--stage);
    font-family: "Poppins", sans-serif;
  }
  .stage {
    width: 1200px; height: 1200px;
    display: flex; flex-direction: column; align-items: center; justify-content: center;
    gap: 44px;
  }
  .card {
    width: 900px; height: 514px; position: relative; overflow: hidden;
    box-shadow: 0 14px 30px rgba(0,0,0,.5);
  }
  /* Front */
  .card-front {
    background: linear-gradient(100deg, var(--green-mid) 0%, var(--green-light) 48%, var(--green-mid) 100%);
    display: flex; align-items: center; justify-content: center;
  }
  .brand { display: flex; align-items: center; gap: 26px; }
  .brand-dot { border-radius: 50%; flex: none; }
  .card-front .brand-dot { width: 92px; height: 92px; background: var(--paper); }
  .brand-text { display: flex; flex-direction: column; }
  .brand-name { font-weight: 700; line-height: 1; letter-spacing: 1px; }
  .brand-tag { font-weight: 500; letter-spacing: 2px; margin-top: 6px; }
  .card-front .brand-name { font-size: 86px; color: var(--paper); }
  .card-front .brand-tag { font-size: 26px; color: var(--paper); }

  /* Back */
  .card-back { background: var(--paper); }
  .card-back .brand { position: absolute; left: 70px; top: 62px; }
  .card-back .brand-dot { width: 76px; height: 76px; background: var(--green-soft); }
  .card-back .brand-name { font-size: 72px; color: var(--green-deep); }
  .card-back .brand-tag { font-size: 23px; color: var(--green-deep); }

  .person { position: absolute; left: 70px; top: 232px; }
  .person-name { font-size: 34px; font-weight: 700; color: var(--green-deep); line-height: 1.1; }
  .person-role { font-size: 21px; color: var(--green-soft); letter-spacing: .5px; }
  .rule { position: absolute; left: 70px; right: 70px; top: 318px; height: 2px; background: var(--green-deep); }

  .contacts {
    position: absolute; left: 70px; right: 60px; top: 340px;
    display: flex; align-items: stretch; gap: 26px;
    font-size: 20px; color: var(--ink);
  }
  .contact-col { display: flex; flex-direction: column; gap: 4px; justify-content: center; }
  .divider { width: 2px; background: var(--green-soft); }
  .contact-row { display: flex; align-items: center; gap: 10px; line-height: 1.4; }
  .icon { width: 22px; height: 22px; flex: none; }
  .address { line-height: 1.35; }
  .band {
    position: absolute; left: 0; right: 0; bottom: 0; height: 24px;
    background: linear-gradient(90deg, var(--green-mid), var(--green-light));
  }
</style>
</head>
<body>
<main class="stage">

  <section class="card card-front" aria-label="Card front">
    <div class="brand">
      <span class="brand-dot"></span>
      <div class="brand-text">
        <span class="brand-name">Loopwise</span>
        <span class="brand-tag">Resource Recovery</span>
      </div>
    </div>
  </section>

  <section class="card card-back" aria-label="Card back">
    <div class="brand">
      <span class="brand-dot"></span>
      <div class="brand-text">
        <span class="brand-name">Loopwise</span>
        <span class="brand-tag">Resource Recovery</span>
      </div>
    </div>

    <div class="person">
      <p class="person-name">Nora K. Bell</p>
      <p class="person-role">Executive Director</p>
    </div>
    <div class="rule"></div>

    <div class="contacts">
      <div class="contact-col">
        <div class="contact-row">
          <svg class="icon" viewBox="0 0 22 22" aria-hidden="true"><circle cx="11" cy="11" r="11" fill="#6abf45"/><rect x="7.5" y="5" width="7" height="12" rx="1.2" fill="none" stroke="#fff" stroke-width="1.5"/></svg>
          <span>123-456-7890</span>
        </div>
        <div class="contact-row">
          <svg class="icon" viewBox="0 0 22 22" aria-hidden="true"><circle cx="11" cy="11" r="11" fill="#6abf45"/><rect x="6" y="9" width="10" height="6" rx="1" fill="#fff"/><rect x="8" y="5.5" width="6" height="4" fill="none" stroke="#fff" stroke-width="1.3"/></svg>
          <span>123-456-7890</span>
        </div>
        <div class="contact-row">
          <svg class="icon" viewBox="0 0 22 22" aria-hidden="true"><circle cx="11" cy="11" r="11" fill="#6abf45"/><path d="M8 6c-1 1-1.5 2.5-.5 4.5s3 4 4.5 4.5 2.5.5 3.5-.5l-1.8-1.8-1.2.8c-1-.5-2.2-1.7-2.7-2.7l.8-1.2z" fill="#fff"/></svg>
          <span>123-456-7890</span>
        </div>
      </div>
      <div class="divider"></div>
      <div class="contact-col">
        <div class="contact-row">
          <svg class="icon" viewBox="0 0 22 22" aria-hidden="true"><circle cx="11" cy="11" r="11" fill="#6abf45"/><rect x="5.5" y="7" width="11" height="8" rx="1" fill="#fff"/><path d="M5.8 7.4 11 11.5l5.2-4.1" fill="none" stroke="#6abf45" stroke-width="1.2"/></svg>
          <span>info@loopwisemail.com</span>
        </div>
        <div class="contact-row">
          <svg class="icon" viewBox="0 0 22 22" aria-hidden="true"><circle cx="11" cy="11" r="11" fill="#6abf45"/><circle cx="11" cy="11" r="5.5" fill="none" stroke="#fff" stroke-width="1.3"/><ellipse cx="11" cy="11" rx="2.4" ry="5.5" fill="none" stroke="#fff" stroke-width="1.1"/><path d="M5.5 11h11" stroke="#fff" stroke-width="1.1"/></svg>
          <span>www.loopwisedepot.com</span>
        </div>
      </div>
      <div class="divider"></div>
      <div class="contact-col address">
        <span>PO BOX 123</span>
        <span>your address</span>
        <span>2nd street london</span>
      </div>
    </div>

    <div class="band"></div>
  </section>

</main>
</body>
</html>
```